Ayurvedic Beauty Company in Need of Business Cards

My company is a high-end ayurvedic beauty brand. I need a business card that represents that. The designer should utilize logo and color palette. I want these cards to be printed with the foil accents so keep that in mind.

I have attached the ai of my logo and business card info. As well as, some of the product we are launching soon, they do not have to be on the card.

Be creative and have fun.

Thanks in advance,

Marla

```html
<!DOCTYPE html>
<html lang="en">
<head>
<meta charset="UTF-8">
<title>Solvani Rose – Business Card</title>
<link href="https://fonts.googleapis.com/css2?family=Montserrat:wght@600;700&family=Roboto:wght@400;500&display=swap" rel="stylesheet">
<style>
  :root {
    --plum: #781d5c;
    --plum-deep: #6a1650;
    --plum-light: #8e3473;
    --gold: #cbb28a;
    --gold-light: #e6d4b3;
    --gold-deep: #b39868;
    --stage: #ebe6df;
  }
  * { margin: 0; padding: 0; box-sizing: border-box; }
  html, body { width: 1200px; height: 950px; overflow: hidden; }
  body {
    background: var(--stage);
    position: relative;
    font-family: "Roboto", Arial, sans-serif;
  }
  .card {
    position: absolute;
    top: 115px;
    width: 420px;
    height: 720px;
    border-radius: 6px;
    overflow: hidden;
    box-shadow: 0 10px 30px rgba(60, 30, 40, 0.25);
  }
  .card--front {
    left: 150px;
    background: linear-gradient(160deg, var(--plum-light) 0%, var(--plum) 40%, var(--plum-deep) 100%);
  }
  .card--back {
    left: 630px;
    background: linear-gradient(170deg, var(--plum) 0%, var(--plum-deep) 100%);
  }

  /* Front */
  .brand {
    position: absolute;
    top: 170px;
    left: 0;
    width: 100%;
    text-align: center;
  }
  .brand__dot {
    display: block;
    width: 110px;
    height: 110px;
    margin: 0 auto 34px;
    border-radius: 50%;
    background: var(--gold);
  }
  .brand__name {
    font-family: "Montserrat", Arial, sans-serif;
    font-weight: 700;
    font-size: 30px;
    letter-spacing: 2px;
    color: var(--gold);
  }
  .wave {
    position: absolute;
    left: 0;
    bottom: 0;
    width: 420px;
    height: 330px;
  }
  .holder {
    position: absolute;
    right: 34px;
    top: 505px;
    text-align: right;
    color: var(--plum);
  }
  .holder__name {
    font-family: "Montserrat", Arial, sans-serif;
    font-weight: 700;
    font-size: 24px;
    letter-spacing: 0.5px;
  }
  .holder__title {
    font-family: "Montserrat", Arial, sans-serif;
    font-weight: 600;
    font-size: 16px;
    margin-top: 2px;
  }
  .contacts {
    list-style: none;
    margin-top: 22px;
  }
  .contacts__item {
    display: flex;
    justify-content: flex-end;
    align-items: center;
    gap: 10px;
    font-size: 16px;
    line-height: 25px;
  }
  .contacts__icon { width: 15px; height: 15px; flex: none; }

  /* Back */
  .back-mark {
    position: absolute;
    top: 40px;
    left: 40px;
    display: flex;
    gap: 6px;
    writing-mode: vertical-rl;
  }
  .back-mark__name {
    font-family: "Montserrat", Arial, sans-serif;
    font-weight: 700;
    font-size: 52px;
    letter-spacing: 2px;
    color: var(--gold);
  }
  .back-mark__site {
    font-size: 17px;
    letter-spacing: 5px;
    color: #f1e6ee;
    padding-top: 8px;
  }
  .products {
    position: absolute;
    right: 30px;
    bottom: 40px;
    width: 200px;
    height: 330px;
    border-radius: 18px;
    background: linear-gradient(180deg, #e5786b 0%, #d8946a 45%, #c99a4a 75%, #8a5a2a 100%);
  }
</style>
</head>
<body>

  <section class="card card--front" aria-label="Business card front">
    <div class="brand">
      <span class="brand__dot" aria-hidden="true"></span>
      <div class="brand__name">SOLVANI ROSE</div>
    </div>

    <svg class="wave" viewBox="0 0 420 330" aria-hidden="true">
      <defs>
        <linearGradient id="goldFoil" x1="0" y1="0" x2="1" y2="1">
          <stop offset="0" stop-color="#e8d7b8"/>
          <stop offset="0.5" stop-color="#cdb48c"/>
          <stop offset="1" stop-color="#b99d6f"/>
        </linearGradient>
      </defs>
      <path d="M0 30 C 110 -10, 230 10, 300 55 C 350 85, 390 90, 420 80 L420 330 L0 330 Z" fill="url(#goldFoil)"/>
      <path d="M0 22 C 110 -18, 230 2, 300 47 C 350 77, 390 82, 420 72" fill="none" stroke="#d9c39c" stroke-width="3"/>
      <path d="M0 40 C 110 0, 230 20, 300 65 C 350 95, 390 100, 420 90" fill="none" stroke="#781d5c" stroke-width="2"/>
    </svg>

    <div class="holder">
      <div class="holder__name">MARLA VANCE</div>
      <div class="holder__title">CEO</div>
      <ul class="contacts">
        <li class="contacts__item">1(888) 555-0142
          <svg class="contacts__icon" viewBox="0 0 16 16" aria-hidden="true"><path d="M3 1l3 3-1.5 2a9 9 0 0 0 5.5 5.5L12 10l3 3-2 2C7 15 1 9 1 3z" fill="#781d5c"/></svg>
        </li>
        <li class="contacts__item">1(347) 555-0187
          <svg class="contacts__icon" viewBox="0 0 16 16" aria-hidden="true"><rect x="3.5" y="0.5" width="9" height="15" rx="1.5" fill="none" stroke="#781d5c" stroke-width="1.5"/><circle cx="8" cy="13" r="1" fill="#781d5c"/></svg>
        </li>
        <li class="contacts__item">marla@lovesolvanirose.com
          <svg class="contacts__icon" viewBox="0 0 16 16" aria-hidden="true"><rect x="0.5" y="3" width="15" height="10" fill="#781d5c"/><path d="M1 3.5l7 5 7-5" fill="none" stroke="#cbb28a" stroke-width="1.2"/></svg>
        </li>
        <li class="contacts__item">www.lovesolvanirose.com
          <svg class="contacts__icon" viewBox="0 0 16 16" aria-hidden="true"><circle cx="8" cy="8" r="7" fill="#781d5c"/><path d="M1 8h14M8 1c-3 4-3 10 0 14M8 1c3 4 3 10 0 14" fill="none" stroke="#cbb28a" stroke-width="1"/></svg>
        </li>
      </ul>
    </div>
  </section>

  <section class="card card--back" aria-label="Business card back">
    <div class="back-mark">
      <span class="back-mark__name">SOLVANI ROSE</span>
      <span class="back-mark__site">solvanirose.com</span>
    </div>
    <div class="products" role="img" aria-label="Photo of two dropper bottles of rose and gold-flake face serum"></div>
  </section>

</body>
</html>
```